Flyer für Hausreinigung
Zielgruppe
Hausverwaltungen, Hausbesitzer.
Aufgabenstellung
Ergebnis soll ein Winword-Dokument mit einem Firmenlogo (Vorschlag: Tintenklecks hellgrün/blau verlaufend mit orangem Besen/Wischer/oder Hand - andere Ideen sind willkommen!) sein, das ich noch um Firmenname/Adresse bzw. Empfängerdaten noch vervollständigen/individualisieren kann. Es soll bunt, aber nicht überladen sein, eventuell mit Stockfotos von lachenden/glücklich schauenden aktiven Menschen sein, jung dynamisch aber nicht flippig. Folgender Text sollte darin vorkommen, Umformulierungen und andere Ideen sind hochwillkommen:
Unser Ziel ist es eine Hausbetreuung fast wie ein Hausbesorger zu leisten, jedoch mit zusätzlichen Vorteilen:
· Der Vertrag ist jederzeit ohne Frist kündbar, ohne Angabe von Gründen!
· Reinigung 1 x pro Woche sowie zusätzliche Bedarfsreinigung
· Krankheits- und Urlaubsvertretung sind bereits inklusive.
· Haftpflichtversicherung über 1,5 Mio. Euro
· Inklusive Gartenbetreuung, Garage, Dachboden, Haustechnik
· Kontrollgänge, 7 x 24 h Erreichbarkeit für Mieter und Eigentümer, Handwerkerüberwachung, Notfallkoordination
· Winterbetreuung der Gehsteige täglich mindestens zwischen 6:00 und 22:00
· Inklusive aller Hilfsmittel und Materialien
· Fixpreis pro Monat.
Nach Möglichkeit soll das auf 1 A4-Seite Platz finden.

```html
<!DOCTYPE html>
<html lang="de">
<head>
<meta charset="utf-8">
<title>Harald Moser – Hausbetreuung</title>
<link href="https://fonts.googleapis.com/css2?family=Open+Sans:ital,wght@0,700;1,400;1,600;1,700&display=swap" rel="stylesheet">
<style>
  :root {
    --sky-top: #4fa3d4;
    --sky-mid: #8cc8e8;
    --wall: #c4e3f2;
    --wall-light: #dcf0f9;
    --swoosh: #ffffff;
    --ink: #111418;
    --name-ink: #3a3a3a;
    --mark: #f2c400;
    --floor-dark: #2a1610;
    --floor-mid: #4a2a1c;
    --chair: #e9e4da;
    --footer-ink: #ffffff;
  }
  * { margin: 0; padding: 0; box-sizing: border-box; }
  html, body { width: 848px; height: 1200px; overflow: hidden; }
  body { font-family: "Open Sans", sans-serif; background: var(--wall); }
  .flyer { position: relative; width: 848px; height: 1200px; overflow: hidden; }
  .backdrop { position: absolute; inset: 0; }
  .brand {
    position: absolute; left: 284px; top: 112px;
    display: flex; align-items: center; gap: 12px;
  }
  .brand-square { width: 66px; height: 66px; background: var(--mark); }
  .brand-name { font-weight: 700; font-size: 32px; color: var(--name-ink); letter-spacing: -0.3px; }
  .content {
    position: absolute; left: 52px; top: 296px; width: 780px;
    transform: rotate(3deg); transform-origin: left top;
    color: var(--ink);
    text-shadow: 2px 3px 4px rgba(0,0,0,0.35);
  }
  .headline {
    font-style: italic; font-weight: 700; font-size: 25.5px; line-height: 1.36;
  }
  .headline span { display: block; padding-left: 26px; }
  .headline span:first-child { padding-left: 0; }
  .benefits {
    list-style: none; margin: 26px 0 0 38px; width: 640px;
    font-style: italic; font-weight: 600; font-size: 17.5px; line-height: 1.3;
  }
  .benefits li::before { content: "· "; }
  .chair {
    position: absolute; left: 469px; top: 820px; width: 312px; height: 292px;
    background: linear-gradient(160deg, #f4f1ea 0%, var(--chair) 55%, #b9ada0 100%);
    border-radius: 8px 8px 2px 2px;
  }
  .floor {
    position: absolute; left: 0; top: 1022px; width: 848px; height: 178px;
    background: linear-gradient(180deg, var(--floor-mid) 0%, var(--floor-dark) 100%);
  }
  .contact {
    position: absolute; left: 0; top: 1156px; width: 848px;
    font-style: italic; font-weight: 600; font-size: 16px; color: var(--footer-ink);
  }
  .contact span { position: absolute; white-space: nowrap; }
</style>
</head>
<body>
<div class="flyer">
  <svg class="backdrop" width="848" height="1200" viewBox="0 0 848 1200" aria-hidden="true">
    <defs>
      <linearGradient id="sky" x1="0" y1="0" x2="0" y2="1">
        <stop offset="0" stop-color="var(--sky-top)"/>
        <stop offset="1" stop-color="var(--sky-mid)"/>
      </linearGradient>
      <linearGradient id="wall" x1="0" y1="0" x2="0" y2="1">
        <stop offset="0" stop-color="var(--wall-light)"/>
        <stop offset="1" stop-color="var(--wall)"/>
      </linearGradient>
    </defs>
    <rect width="848" height="1200" fill="url(#wall)"/>
    <path d="M0 0 H848 V150 C700 250 500 200 330 230 C200 252 90 300 0 330 Z" fill="url(#sky)"/>
    <path d="M0 330 C90 300 200 252 330 230 C500 200 700 250 848 150 V200 C700 290 500 250 330 275 C200 295 90 340 0 375 Z" fill="var(--swoosh)" opacity="0.55"/>
    <path d="M0 0 H848 V60 C650 120 420 40 220 110 C130 140 60 160 0 170 Z" fill="var(--swoosh)" opacity="0.18"/>
  </svg>

  <header class="brand">
    <div class="brand-square"></div>
    <div class="brand-name">Harald Moser</div>
  </header>

  <section class="content">
    <h1 class="headline">
      <span>Unser Ziel ist es eine Hausbetreuung fast wie ein</span>
      <span>Hausbesorger zu leisten, jedoch mit zusätzlichen Vorteilen:</span>
    </h1>
    <ul class="benefits">
      <li>Der Vertrag ist jederzeit ohne Frist kündbar, ohne Angabe von Gründen!</li>
      <li>Reinigung 1 x pro Woche sowie zusätzliche Bedarfsreinigung</li>
      <li>Krankheits- und Urlaubsvertretung sind bereits inklusive.</li>
      <li>Haftpflichtversicherung über 1,5 Mio. Euro</li>
      <li>Inklusive Gartenbetreuung, Garage, Dachboden, Haustechnik</li>
      <li>Kontrollgänge, 7 x 24 h Erreichbarkeit für Mieter und Eigentümer, Handwerkerüberwachung, Notfallkoordination</li>
      <li>Winterbetreuung der Gehsteige täglich mindestens zwischen 6:00 und 22:00</li>
      <li>Inklusive aller Hilfsmittel und Materialien</li>
      <li>Fixpreis pro Monat.</li>
    </ul>
  </section>

  <div class="floor" role="img" aria-label="Dunkler Holzparkettboden"></div>
  <div class="chair" role="img" aria-label="Weißer gepolsterter Sessel mit Holzgestell"></div>

  <footer class="contact">
    <span style="left:94px">Lindengasse 12</span>
    <span style="left:281px">Mödling</span>
    <span style="left:409px">Tel: 0123 456789</span>
    <span style="left:575px">Email: info@moser-hb.at</span>
  </footer>
</div>
</body>
</html>
```